当募集をご覧頂き誠にありがとうございます。 新商品(BBQグリル)のサムネイル画像を制作して頂ける方を募集します。 <お仕事の詳細> 添付素材のいずれかを用いてサムネイル画像を製作してください。商用利用可能なその他素材を足して頂いても結構です。 画像は一部をズームして切り取ったり、明るさ等を調整頂いたりしてOKです。 本商品の参考サイト http://qelmorstock.com/tk-rz4 http://qelmorstock.com/tkvid <希望イメージ> 文字の視認性、インパクトを重視します。 メインターゲットは40代男性となります。 <コピー> メインコピーとして下記5つの内、一つのみを選択してください ・手軽に本格、叶います BBQグリルの革命児 ・思わず2度見!ファブリックBBQグリル ・お手軽BBQをスタイリッシュに ・ファブリックBBQグリルでスタイリッシュに始めよう! ・サプライズBBQの主役!ファブリックグリル ・常識を覆すファブリックBBQグリル <納品形式> PNGファイルと編集可能なファイル サイズ: 横1600 ×縦900 ピクセル、横1200 × 縦800 ピクセル(2種類) ※横1600×縦900 ピクセルサイズでご提案頂き、採用後に追加で横1200×縦800 ピクセルを製作頂きます。 採用者には必要に応じて高画質画像をお渡しします。 <禁止事項> ・著作権は当方に譲渡されますので、流用・転載・売却は禁止とさせて頂きます。 ・当方が提供する、いかなる情報を許可なく漏洩しないこと。 なお、応募は早期に締め切る可能性があります。 以上、ご応募、お待ちしております。 |
どの案も素敵でしたが、こちらのご提案が一番イメージに近かったため採用させて頂きました。
皆様ご提案ありがとうございます。素敵な案ばかりでした。また機会がございましたらよろしくお願い致します。

```html
<!DOCTYPE html>
<html lang="ja">
<head>
<meta charset="utf-8">
<title>ファブリックBBQグリル サムネイル</title>
<link href="https://fonts.googleapis.com/css2?family=Noto+Sans+JP:wght@900&display=swap" rel="stylesheet">
<style>
  :root {
    --yellow: #ffe01a;
    --ink: #141414;
    --red: #e8141c;
    --white: #ffffff;
    --grill-top: #6f6a63;
    --grill-mid: #c99c7e;
    --field-top: #8a9a86;
    --field-bottom: #6f8f3a;
  }
  html, body {
    margin: 0;
    padding: 0;
    overflow: hidden;
    background: var(--white);
  }
  .thumbnail {
    position: relative;
    width: 1200px;
    height: 676px;
    overflow: hidden;
    font-family: "Noto Sans JP", sans-serif;
    font-weight: 900;
  }
  .photo {
    position: absolute;
    right: 0;
    width: 660px;
  }
  .photo--grilling {
    top: 0;
    height: 300px;
    background: linear-gradient(160deg, #e9e4de 0%, var(--grill-mid) 45%, var(--grill-top) 100%);
  }
  .photo--products {
    top: 300px;
    height: 376px;
    background: linear-gradient(180deg, var(--field-top) 0%, #9aa48c 45%, var(--field-bottom) 100%);
  }
  .copy-panel {
    position: absolute;
    inset: 0;
    width: 1200px;
    height: 676px;
  }
  .brand {
    position: absolute;
    left: 36px;
    top: 36px;
    width: 132px;
    height: 132px;
    border-radius: 50%;
    background: var(--ink);
    display: flex;
    align-items: center;
    justify-content: center;
    text-align: center;
    color: var(--white);
    font-size: 19px;
    line-height: 1.15;
    letter-spacing: 0.04em;
  }
  .headline {
    position: absolute;
    margin: 0;
    line-height: 1;
    white-space: nowrap;
  }
  .headline--lead {
    color: var(--ink);
    font-size: 122px;
    letter-spacing: 0.02em;
    text-align: center;
    left: 216px;
    top: 68px;
  }
  .headline--lead span { display: block; margin-bottom: 12px; }
  .headline--product {
    color: var(--red);
    font-size: 124px;
    letter-spacing: -0.02em;
    left: 128px;
    top: 330px;
    -webkit-text-stroke: 14px var(--white);
    paint-order: stroke fill;
  }
  .headline--product span { display: block; margin-bottom: 22px; }
  .headline--product .latin { letter-spacing: 0.04em; }
</style>
</head>
<body>
  <main class="thumbnail">
    <div class="photo photo--grilling" role="img" aria-label="網の上で焼かれる大きな海老をトングでつかむ様子"></div>
    <div class="photo photo--products" role="img" aria-label="芝生の上に並ぶ黒と赤のファブリックBBQグリル"></div>

    <svg class="copy-panel" viewBox="0 0 1200 676" aria-hidden="true">
      <polygon points="0,0 582,0 472,676 0,676" fill="var(--yellow)"/>
    </svg>

    <div class="brand">EMBERTO<br>GRILLS</div>

    <h1 class="headline headline--lead">
      <span>思わず</span>
      <span>2度見!</span>
    </h1>

    <p class="headline headline--product">
      <span>ファブリック</span>
      <span class="latin">BBQグリル</span>
    </p>
  </main>
</body>
</html>
```